Upgrade my Web to PHP format

I need move my web site http://qrnlivo7.example to PHP format my hosting is running under Linux with MySQL , all information is on old Web site and we need move to the new Web Design , We would like to see designs that use the color of our logo.

The final design should communicate about security software , security services and hosting Vorlan Stride k server.

Is very important easy installation and instructions of installation.

Target Market(s)

Bank and security company

Industry/Entity Type

Computer Security

Number of Pages Required

5+ page

Font styles to use
Sans Serif
Other font styles liked:
• arial, verdana.

Colors
3276b5
33a6d7
85cae6
85acd3
88d0c7

Requirements
Must have
• respect to our colors and all link to all pages, videos , and PDF.
Nice to have
• I would like design about security server and services , developer software security.
Should not have
• Anti Virus

```html
<!DOCTYPE html>
<html lang="en">
<head>
<meta charset="utf-8">
<title>QV Support</title>
<link href="https://fonts.googleapis.com/css2?family=Open+Sans:wght@400;600;700&display=swap" rel="stylesheet">
<style>
:root{
  --brand:#3276b5;
  --sky:#33a6d7;
  --ice:#85cae6;
  --steel:#85acd3;
  --ink:#2f2f2f;
  --text:#6b6b6b;
  --line:#e3e3e3;
  --footer:#3a3a3a;
  --footer-deep:#2c2c2c;
  --white:#ffffff;
}
*{margin:0;padding:0;box-sizing:border-box}
html,body{width:1200px;height:3593px;overflow:hidden;background:var(--white)}
body{font-family:"Open Sans",Arial,sans-serif;color:var(--text);position:relative}
.abs{position:absolute}
.wrap{position:absolute;left:98px;width:1004px}

/* header */
.site-header{top:0;left:0;width:1200px;height:77px;background:var(--white)}
.brand{position:absolute;left:100px;top:20px;display:flex;align-items:center;gap:10px}
.brand-dot{width:36px;height:36px;border-radius:50%;background:var(--brand)}
.brand-name{font-size:24px;font-weight:700;color:var(--brand);letter-spacing:.5px}
.main-nav a{position:absolute;top:30px;font-size:13px;color:#555;text-decoration:none}

/* hero */
.hero{top:77px;left:0;width:1200px;height:534px;background:linear-gradient(100deg,#2c3a48 0%,#4d6275 45%,#7c8fa0 70%,#3d4f61 100%)}
.hero-photo{position:absolute;left:470px;top:0;width:730px;height:534px;background:radial-gradient(ellipse at 55% 40%,rgba(200,215,230,.35),rgba(40,55,70,0) 70%)}
.hero-title{position:absolute;left:100px;top:146px;font-size:40px;font-weight:600;color:var(--white)}
.hero-sub{position:absolute;left:100px;top:197px;font-size:26px;color:var(--ice)}
.hero-copy{position:absolute;left:100px;top:250px;width:420px;font-size:13px;line-height:20px;color:var(--white)}
.btn{display:inline-flex;align-items:center;justify-content:center;height:46px;padding:0 38px;border-radius:23px;background:var(--sky);color:var(--white);font-size:12px;font-weight:700;letter-spacing:.3px;text-decoration:none}
.hero .btn{position:absolute;left:103px;top:344px;width:192px;padding:0}
.hero-prev{position:absolute;left:40px;top:244px;width:28px;height:28px;border-radius:50%;background:rgba(255,255,255,.15);display:flex;align-items:center;justify-content:center}

/* centered sections */
.section-title{font-size:25px;font-weight:700;color:var(--ink);text-align:center;letter-spacing:.3px}
.section-sub{font-size:19px;color:#8a8a8a;text-align:center;margin-top:8px}
.section-copy{font-size:13.5px;line-height:26px;text-align:center;margin:18px auto 0;width:840px}
.welcome{top:685px}
.integrating{top:878px}
.services{top:1050px;display:flex;justify-content:space-between;padding:0 40px}
.service{width:170px;text-align:center}
.service svg{display:block;margin:0 auto}
.service-name{margin-top:24px;font-size:12.5px;font-weight:700;color:var(--ink);line-height:20px}

/* principles band */
.principles{top:1284px;left:0;width:1200px;height:501px;background:radial-gradient(ellipse at 50% 110%,#2a5aa8 0%,#183e84 35%,#0f2a61 70%,#0b1f4a 100%)}
.principles .section-title{position:absolute;top:80px;width:1200px;color:var(--white)}
.principles-copy{position:absolute;top:136px;left:170px;width:860px;text-align:center;color:#e4ecf7;font-size:14px;line-height:28px}
.principles-copy p+p{margin-top:8px}
.tech-row{position:absolute;top:310px;left:172px;width:860px;display:flex;justify-content:space-between;align-items:center;color:var(--white);font-size:14px;font-weight:700}
.tech-row .arrow{color:#9db4d8;font-weight:400}
.principles .btn{position:absolute;left:504px;top:379px;width:192px;padding:0}

/* datacenter */
.datacenter-media{top:1861px;left:98px;width:455px;height:287px;background:linear-gradient(135deg,#e9eef3 0%,#c8d4de 50%,#9fb3c4 100%)}
.play{position:absolute;left:197px;top:113px;width:62px;height:62px;border-radius:50%;background:rgba(255,255,255,.85);border:2px solid var(--brand);display:flex;align-items:center;justify-content:center}
.datacenter-text{top:1862px;left:616px;width:486px}
.datacenter-text h2{font-size:24px;font-weight:700;color:var(--ink)}
.datacenter-text p{font-size:13px;line-height:25px;margin-top:18px}
.datacenter-text h2+p{margin-top:20px}

/* posts */
.posts-title{top:2232px}
.posts{top:2309px;display:flex;justify-content:space-between}
.post{width:304px}
.post-image{height:182px}
.post h3{margin-top:30px;font-size:12.5px;font-weight:700;color:var(--ink)}
.post-date{font-size:11px;color:#8f8f8f;margin-top:4px}
.post-rule{width:58px;height:3px;background:var(--brand);margin:17px 0 20px}
.post p{font-size:12px;line-height:24px}

/* testimonials */
.testimonials-title{top:2722px}
.testimonials{top:2802px;display:flex}
.quote{width:502px;display:flex;gap:30px;padding-left:17px}
.avatar{width:117px;height:117px;border-radius:50%;flex:none;background:radial-gradient(circle at 50% 40%,#e6d7cc 0%,#b9a89c 55%,#d9dde2 100%)}
.quote-name{font-size:12.5px;font-weight:700;color:var(--brand);margin-top:6px}
.quote-role{font-size:11px;color:#8f8f8f;margin-top:2px}
.quote p{font-size:12px;line-height:24px;margin-top:10px;width:330px}
.dots{top:2970px;left:0;width:1200px;display:flex;justify-content:center;gap:9px}
.dots span{width:8px;height:8px;border-radius:50%;background:#d7d7d7}
.dots span.on{background:#7fbf3f}

/* partners */
.partners{top:3063px;display:flex;justify-content:space-between}
.partner{width:186px;height:103px;border:1px solid var(--line);box-shadow:0 1px 3px rgba(0,0,0,.08);display:flex;align-items:center;justify-content:center;font-size:17px;font-weight:700;color:var(--brand)}

/* footer */
.site-footer{top:3233px;left:0;width:1200px;height:287px;background:var(--footer)}
.foot-col{position:absolute;top:46px}
.foot-col h4{font-size:12px;font-weight:700;color:var(--white);letter-spacing:.3px;margin-bottom:10px}
.foot-col a{display:block;font-size:11px;line-height:24px;color:#b3b3b3;text-decoration:none}
.foot-bar{top:3520px;left:0;width:1200px;height:73px;background:var(--footer-deep)}
.foot-brand{position:absolute;left:100px;top:23px;display:flex;align-items:center;gap:8px}
.foot-brand span.dot{width:26px;height:26px;border-radius:50%;background:#8a8a8a}
.foot-brand b{font-size:18px;color:#8a8a8a;font-weight:700}
.copyright{position:absolute;left:295px;top:28px;font-size:11px;color:#8f8f8f}
.social{position:absolute;left:912px;top:29px;display:flex;gap:22px}
.social span{width:14px;height:14px;border-radius:50%;background:#8f8f8f}
</style>
</head>
<body>

<header class="site-header abs">
  <div class="brand"><span class="brand-dot"></span><span class="brand-name">QVSUPPORT</span></div>
  <nav class="main-nav">
    <a style="left:470px">About</a>
    <a style="left:563px">Products</a>
    <a style="left:673px">Services</a>
    <a style="left:777px">Cloud Services</a>
    <a style="left:917px">Contact</a>
    <a style="left:1020px">Support Ticket</a>
  </nav>
</header>

<section class="hero abs">
  <div class="hero-photo" role="img" aria-label="Businessman touching a cloud icon surrounded by device and network icons"></div>
  <div class="hero-prev"><svg width="10" height="12" viewBox="0 0 10 12"><path d="M7 1 2 6l5 5" fill="none" stroke="#fff" stroke-width="2"/></svg></div>
  <h1 class="hero-title">QV Support</h1>
  <div class="hero-sub">We provide hosting Vorlan Stride k server</div>
  <p class="hero-copy">Lorem Ipsum is simply dummy text of the printing and typesetting industry. Lorem Ipsum has been the industry's standard dummy text ever since the 1500s, when an unknown printer...</p>
  <a class="btn">VIEW MORE DETAILS</a>
</section>

<section class="wrap welcome">
  <h2 class="section-title">WELCOME TO QV SUPPORT</h2>
  <div class="section-sub">We offer security server and services, develop software security</div>
  <p class="section-copy">Our certified IT technicians and computer engineers excel with design, deployment, and maintaining communications systems. From implementing new data management systems to upgrading security standards, we can handle all your IT needs.</p>
</section>

<section class="wrap integrating">
  <h2 class="section-title">INTEGRATING IT SERVICES</h2>
  <p class="section-copy">QVSUPPORT boasts an incredible number of skilled and experienced IT technicians, allowing us to be a leader in the field. We deal with businesses of all sorts, providing a variety of services to ensure your company information is secure and your business operations stay up and running around the clock.</p>
</section>

<section class="wrap services">
  <div class="service">
    <svg width="110" height="80" viewBox="0 0 110 80" fill="none" stroke="#3276b5" stroke-width="2.5" stroke-linejoin="round" stroke-linecap="round">
      <path d="M4 30 22 14l14 10M106 30 88 14 70 22H52l-12 12 6 6 14-8 30 24"/>
      <path d="M22 14 4 30l34 34 6-6M44 58l8 8 6-6M52 66l6 6 6-6M60 58l8 8 8-8"/>
    </svg>
    <div class="service-name">CONSULTING &amp;<br>IMPLEMENTATION</div>
  </div>
  <div class="service">
    <svg width="110" height="80" viewBox="0 0 110 80" fill="none" stroke="#3276b5" stroke-width="2.5" stroke-linecap="round">
      <rect x="12" y="6" width="86" height="56" rx="2"/>
      <path d="M20 18h70M24 30h18M48 30h38M24 40h30M60 40h26M24 50h50M44 62v10M66 62v10M34 74h42"/>
    </svg>
    <div class="service-name">APPLICATION<br>DEVELOPMENT</div>
  </div>
  <div class="service">
    <svg width="110" height="80" viewBox="0 0 110 80" fill="none" stroke="#3276b5" stroke-width="2.5" stroke-linejoin="round" stroke-linecap="round">
      <path d="M55 4 28 14v24c0 18 12 30 27 38 15-8 27-20 27-38V14z"/>
      <path d="M42 40l9 9 18-20"/>
    </svg>
    <div class="service-name">TESTING, ANALYSIS AND<br>SECURITY DIAGNOSIS</div>
  </div>
  <div class="service">
    <svg width="110" height="80" viewBox="0 0 110 80" fill="none" stroke="#3276b5" stroke-width="2.5" stroke-linecap="round">
      <path d="M22 40a33 33 0 0 1 56-24M88 40a33 33 0 0 1-56 24"/>
      <path d="M78 6v10H68M32 74V64h10"/>
      <path d="M44 52V40M52 52V32M60 52V36M68 52V44"/>
    </svg>
    <div class="service-name">UPGRADING<br>SYSTEMS</div>
  </div>
</section>

<section class="principles abs" role="img" aria-label="Night view of the earth from space with city lights">
  <h2 class="section-title">EFFECTIVE OPERATING PRINCIPLES</h2>
  <div class="principles-copy">
    <p>We are a company with extensive experience in the area of information technology for environments Vorlan Stride k (KS/480), and we are part of the ISV Business Partners.</p>
    <p>Our strength lies in the extensive knowledge and experience in the area of computer security and support in providing the best solutions, which cover the requirements of confidentiality and availability of data on that platform.</p>
  </div>
  <div class="tech-row">
    <span>RPX</span><span class="arrow">&rarr;</span><span>RPXLE</span><span class="arrow">&rarr;</span><span>NX FRAME 2010</span><span class="arrow">&rarr;</span><span>WEBPAGE.KIT</span><span class="arrow">&rarr;</span><span>DQ4</span><span class="arrow">&rarr;</span><span>QRY SERVER</span>
  </div>
  <a class="btn">VIEW MORE DETAILS</a>
</section>

<div class="datacenter-media abs" role="img" aria-label="Hand holding a tablet showing email messages, video preview">
  <div class="play"><svg width="20" height="22" viewBox="0 0 20 22"><path d="M4 2l14 9L4 20z" fill="#3276b5"/></svg></div>
</div>
<section class="datacenter-text abs">
  <h2>DATACENTER SERVICES</h2>
  <p>We offer rental services for virtual servers KS/480 user or equipment, also hosting server placement and Vindara, Lynox, Onyx servers.</p>
  <p>We specialize in providing secure high-speed connections to an Vorlan Stride k (KS/480) via Internet.</p>
  <p>From hosting managed by our technicians, programmers with basic accounts, QVSupport Portvale has a service to meet their business objectives of our new DataCenter dare in Corvela.</p>
</section>

<h2 class="wrap section-title posts-title">RECENT POSTS</h2>
<section class="wrap posts">
  <article class="post">
    <div class="post-image" role="img" aria-label="Blue arrows with big data lettering" style="background:linear-gradient(135deg,#d9e8f5,#3f86d0 60%,#1c5ca8)"></div>
    <h3>LOREM IPSUM IS SIMPLY DUMMY TEXT</h3>
    <div class="post-date">Posted on 27 March 2015</div>
    <div class="post-rule"></div>
    <p>Lorem Ipsum is simply dummy text of the printing and typesetting industry. Lorem Ipsum has been the industry's standard dummy text ever since the 1500s.</p>
  </article>
  <article class="post">
    <div class="post-image" role="img" aria-label="Tablet with business charts on a desk" style="background:linear-gradient(135deg,#f4f5f7,#d5dbe2 55%,#9aa8b6)"></div>
    <h3>LOREM IPSUM IS SIMPLY DUMMY TEXT</h3>
    <div class="post-date">Posted on 27 March 2015</div>
    <div class="post-rule"></div>
    <p>Lorem Ipsum is simply dummy text of the printing and typesetting industry. Lorem Ipsum has been the industry's standard dummy text ever since the 1500s.</p>
  </article>
  <article class="post">
    <div class="post-image" role="img" aria-label="Glowing world network map" style="background:radial-gradient(ellipse at 50% 45%,#3b8fe0,#0d3a80 60%,#061b44)"></div>
    <h3>LOREM IPSUM IS SIMPLY DUMMY TEXT</h3>
    <div class="post-date">Posted on 27 March 2015</div>
    <div class="post-rule"></div>
    <p>Lorem Ipsum is simply dummy text of the printing and typesetting industry. Lorem Ipsum has been the industry's standard dummy text ever since the 1500s.</p>
  </article>
</section>

<h2 class="wrap section-title testimonials-title">TESTIMONIALS</h2>
<section class="wrap testimonials">
  <div class="quote">
    <div class="avatar" role="img" aria-label="Portrait of the client"></div>
    <div>
      <div class="quote-name">Milo Carden</div>
      <div class="quote-role">Business man</div>
      <p>Lorem Ipsum is simply dummy text of the printing and typesetting industry. Lorem Ipsum has been the industry's standard dummy text ever since the 1500s.</p>
    </div>
  </div>
  <div class="quote">
    <div class="avatar" role="img" aria-label="Portrait of the client"></div>
    <div>
      <div class="quote-name">Milo Carden</div>
      <div class="quote-role">Business man</div>
      <p>Lorem Ipsum is simply dummy text of the printing and typesetting industry. Lorem Ipsum has been the industry's standard dummy text ever since the 1500s.</p>
    </div>
  </div>
</section>
<div class="dots abs"><span class="on"></span><span></span><span></span></div>

<section class="wrap partners">
  <div class="partner">Banvera</div>
  <div class="partner">Corvesco</div>
  <div class="partner">Banco Ultramar</div>
  <div class="partner">Tecnavo</div>
  <div class="partner">Ulterior</div>
</section>

<footer class="site-footer abs">
  <div class="foot-col" style="left:103px">
    <h4>WELCOME</h4>
    <a>Home</a><a>About</a><a>Products</a><a>Services</a><a>Cloud Services</a><a>Contact</a><a>Support Ticket</a>
  </div>
  <div class="foot-col" style="left:299px">
    <h4>SOLUTIONS</h4>
    <a>Education</a><a>Workspace</a><a>Customers Stories</a>
  </div>
  <div class="foot-col" style="left:496px">
    <h4>HELP</h4>
    <a>Tutorials</a><a>Tech Support</a><a>Community Support</a><a>Lost Software Key</a>
  </div>
  <div class="foot-col" style="left:692px">
    <h4>COMPANY</h4>
    <a>About</a><a>Contact</a><a>Blog</a><a>Connect with Us</a><a>Careers</a><a>Partner Programs</a><a>Press Room</a>
  </div>
  <div class="foot-col" style="left:915px">
    <h4>STORE</h4>
    <a>Personal and Professional</a><a>Volume Licensing</a><a>Education</a><a>Government and Non-Profit</a><a>Find a Reseller</a><a>Online Store FAQ</a><a>Payment Options</a>
  </div>
</footer>

<div class="foot-bar abs">
  <div class="foot-brand"><span class="dot"></span><b>QVSUPPORT</b></div>
  <div class="copyright">&copy; 2015, QV Support. All Rights Reserved.</div>
  <div class="social"><span></span><span></span><span></span><span></span><span></span><span></span></div>
</div>

</body>
</html>
```